Internal web page of multinational company - Portfolio of reports

We need to improve the look & feel of an existing internal HTML page.
We use it as a portfolios where users go and see a list of existing reports as "tiles". The HTML page is automatically generated by a javascript that reads the contents to display from an HTML file.
What is needs is a "face lift" in the design of the page.
Currently we use icons on the top right of each tile to denote the type of technology used on the report and also colons for the same purpose. The attached screenshots will be self explanatory.
Across the top we have "tabs" that, once selected change the tiles.
Need a proposal for new design that keeps is as clean as possible, specially the home page that should be very light (Wextor like).
The idea for this page is to serve as a "one stop shop" and become a bookmark for everyone in the company.
Looking for a wow effect that make is visually

Internal employees

It Company

2 page

• Should not change the logo or its position from the bottom left.
• Page must be as clean as possible and
• Welcome to change the logo on the top left. This page is from the KPT R&M (Rnm) which stands for Knowledge Pooling Team - Reporting & Modelling.
• Do no use red, this is the color of our competitor. The blue on the bottom is standard for our logo

```html
<!DOCTYPE html>
<html lang="en">
<head>
<meta charset="utf-8">
<title>Knowledge Pooling Portfolio</title>
<link href="https://fonts.googleapis.com/css2?family=Open+Sans:wght@400;600&family=Raleway:wght@500;600&display=swap" rel="stylesheet">
<style>
  :root {
    --header-top: #ffffff;
    --header-bottom: #eeeeee;
    --header-line: #c9c9c9;
    --brand-text: #3a3f4a;
    --footer-blue: #0b4094;
    --footer-text: #e6ecf7;
    --photo-light: #f4f4f4;
    --photo-mid: #e2e2e2;
    --photo-dark: #cfcfcf;
    --tile-border: #ffffff;
    --hr-top: #55d6f0;
    --hr-bottom: #2bb8dc;
    --finance-top: #1c95e6;
    --finance-bottom: #0a62c8;
    --ps-top: #22b6de;
    --ps-bottom: #0a89b9;
    --kpt-top: #ffb800;
    --kpt-bottom: #ff8600;
    --dist-top: #10308f;
    --dist-bottom: #061863;
    --search-border: #cfcfcf;
    --search-text: #555555;
  }
  * { box-sizing: border-box; margin: 0; padding: 0; }
  html, body { width: 1200px; height: 722px; overflow: hidden; background: #ffffff; }
  .page { position: relative; width: 1200px; height: 722px; overflow: hidden; font-family: "Open Sans", sans-serif; }

  .hero-photo {
    position: absolute; left: 0; top: 74px; width: 1200px; height: 589px;
    background:
      radial-gradient(ellipse 260px 320px at 600px 330px, var(--photo-dark), transparent 70%),
      radial-gradient(ellipse 220px 300px at 900px 300px, var(--photo-mid), transparent 72%),
      linear-gradient(180deg, var(--photo-light), var(--photo-mid));
  }

  .site-header {
    position: absolute; left: 0; top: 0; width: 1200px; height: 74px;
    background: linear-gradient(180deg, var(--header-top), var(--header-bottom));
    border-bottom: 1px solid var(--header-line);
  }
  .brand-name {
    position: absolute; left: 142px; top: 26px;
    font-family: "Open Sans", sans-serif; font-weight: 600; font-size: 15px; line-height: 20px;
    color: var(--brand-text);
  }

  .search {
    position: absolute; left: 838px; top: 23px; width: 223px; height: 28px;
    display: flex; border: 1px solid var(--search-border); background: #ffffff;
  }
  .search-field { flex: 1; font-size: 11px; color: var(--search-text); padding: 6px 10px; }
  .search-button, .search-clear {
    width: 29px; border-left: 1px solid var(--search-border);
    display: flex; align-items: center; justify-content: center; color: #999999; font-size: 12px;
  }

  .portfolio-tiles { position: absolute; left: 0; top: 0; }
  .tile {
    position: absolute; width: 274px; height: 52px;
    border: 3px solid var(--tile-border);
    box-shadow: 0 1px 4px rgba(0,0,0,0.18);
    display: flex; align-items: center; justify-content: center;
    font-family: "Raleway", sans-serif; font-weight: 600; font-size: 21px; color: #ffffff;
  }
  .tile-hr { left: 314px; top: 232px; background: linear-gradient(180deg, var(--hr-top), var(--hr-bottom)); }
  .tile-finance { left: 615px; top: 232px; background: linear-gradient(180deg, var(--finance-top), var(--finance-bottom)); }
  .tile-ps { left: 314px; top: 309px; background: linear-gradient(180deg, var(--ps-top), var(--ps-bottom)); }
  .tile-kpt { left: 615px; top: 309px; background: linear-gradient(180deg, var(--kpt-top), var(--kpt-bottom)); }
  .tile-distribution { left: 463px; top: 392px; background: linear-gradient(180deg, var(--dist-top), var(--dist-bottom)); }

  .site-footer { position: absolute; left: 0; top: 663px; width: 1200px; height: 59px; background: var(--footer-blue); }
  .legal { position: absolute; left: 142px; top: 20px; font-size: 12.5px; color: var(--footer-text); }
  .social { position: absolute; left: 985px; top: 21px; display: flex; gap: 10px; }
  .social-dot { width: 15px; height: 15px; border-radius: 50%; background: #ffffff; }
  .page-code { position: absolute; right: 6px; bottom: 3px; font-size: 11px; color: var(--footer-text); }
</style>
</head>
<body>
<div class="page">
  <div class="hero-photo" role="img" aria-label="Soft grey photograph of two businessmen reviewing documents and a tablet at a table"></div>

  <header class="site-header">
    <div class="brand-name">Knowledge Pooling Portfolio</div>
    <div class="search">
      <div class="search-field">Search here</div>
      <div class="search-button">
        <svg width="14" height="14" viewBox="0 0 14 14" aria-hidden="true"><circle cx="6" cy="6" r="4.5" fill="none" stroke="#999" stroke-width="1.8"/><line x1="9.3" y1="9.3" x2="13" y2="13" stroke="#999" stroke-width="2"/></svg>
      </div>
      <div class="search-clear">X</div>
    </div>
  </header>

  <nav class="portfolio-tiles">
    <div class="tile tile-hr">HR</div>
    <div class="tile tile-finance">FINANCE</div>
    <div class="tile tile-ps">P &amp; S</div>
    <div class="tile tile-kpt">KPT</div>
    <div class="tile tile-distribution">DISTRIBUTION</div>
  </nav>

  <footer class="site-footer">
    <div class="legal">© 2015 Company Name &nbsp;All right reserved &nbsp;Term of Use</div>
    <div class="social">
      <span class="social-dot" aria-label="Social link"></span>
      <span class="social-dot" aria-label="Social link"></span>
      <span class="social-dot" aria-label="Social link"></span>
    </div>
    <div class="page-code">X14</div>
  </footer>
</div>
</body>
</html>
```